Wix web design for healthcare IT consulting firm.

I am looking for a web design built in Wix that it will be easy for me to add or edit content in the future. The web site does not need to be overly complicated, but it should look very polished and professional. I also want to ensure it is mobile device friendly. I do not need any type of on-line purchasing ability. I will eventually do blogs, but for now it is a fairly standard web site with main page, about us, services provided, etc. I would also like a place for potential customers to contact us directly from the web site. I have included a Word document with some content for the web design. I have also included my logo and business card for reference. I would like to utilize similar colors as my business card. One of my primary competitors is https://vonmarlhq.example/

Target Market(s)

Target market could be nursing home CEO, CIO, or other leader at an organization that manages long term care facilities.

Number of Pages Required

5+ page

Colors
876aae

Requirements
Must have
• Be designed to be used in Wix. Use the content I provided to create and make web design. Allow to be viewed on mobile device. Please use similar color structure as attached business card. Please use attached logo in design.

```html
<!DOCTYPE html>
<html lang="en">
<head>
<meta charset="utf-8">
<title>ClearPath Health – Healthcare Solutions</title>
<link rel="stylesheet" href="https://fonts.googleapis.com/css2?family=Montserrat:wght@400;500;600;700&family=Open+Sans:wght@400;600;700&display=swap">
<style>
:root{
  --purple:#6a3fa6;
  --purple-dark:#56308a;
  --purple-soft:#8a6ac0;
  --lavender:#f4f1f9;
  --ink:#1d1d24;
  --text:#55525e;
  --muted:#8c8896;
  --white:#ffffff;
  --footer:#121115;
  --line:#d8d2e4;
}
*{box-sizing:border-box;margin:0;padding:0}
html,body{width:1200px;height:4592px;overflow:hidden}
body{font-family:"Open Sans",Arial,sans-serif;color:var(--text);background:var(--white);position:relative}
h1,h2,h3,h4{font-family:"Montserrat",Arial,sans-serif}
section,header,footer{position:absolute;left:0;width:1200px}

/* header */
.site-header{top:0;height:98px;background:var(--purple);z-index:2}
.brand{position:absolute;left:78px;top:12px;width:194px;height:72px;border:2px solid var(--white);padding:6px 10px;color:var(--white)}
.brand-name{font-family:"Montserrat",sans-serif;font-weight:700;font-size:30px;line-height:34px}
.brand-tag{font-size:10px;letter-spacing:1.5px;font-weight:600}
.phone{position:absolute;right:78px;top:10px;color:var(--white);font-family:"Montserrat",sans-serif;font-weight:600;font-size:22px;display:flex;align-items:center;gap:10px}
.main-nav{position:absolute;right:78px;top:56px;display:flex;gap:30px;align-items:center;color:var(--white);font-family:"Montserrat",sans-serif;font-size:14px;font-weight:500}
.search{width:30px;height:30px;border-radius:50%;background:var(--white);display:flex;align-items:center;justify-content:center}

/* hero */
.hero{top:98px;height:575px}
.hero-photo{position:absolute;inset:0;background:linear-gradient(100deg,#6c7b88 0%,#c7ccd0 35%,#e9eaec 60%,#dcdcdf 100%)}
.hero-copy{position:absolute;right:78px;top:145px;width:600px;text-align:right}
.hero-copy h1{font-size:37px;line-height:50px;font-weight:700;color:#232230;text-transform:uppercase}
.hero-copy h1 span{color:var(--purple)}
.hero-copy p{font-size:16px;color:#2c2b33;margin-top:6px}
.btn{display:inline-block;font-family:"Montserrat",sans-serif;font-weight:600;font-size:16px;letter-spacing:.5px}
.btn-solid{background:var(--purple);color:var(--white);padding:15px 24px;margin-top:26px}
.arrow{position:absolute;top:235px;width:46px;height:46px;border-radius:50%;background:rgba(255,255,255,.5);display:flex;align-items:center;justify-content:center}

/* welcome */
.welcome{top:673px;height:435px;text-align:center}
.welcome h2{margin-top:58px;font-size:40px;color:var(--purple);font-weight:700}
.welcome .sub{font-size:13px;letter-spacing:1px;margin-top:4px;color:#444}
.welcome p.body{width:760px;margin:22px auto 0;font-size:14px;line-height:26px;color:var(--muted)}
.welcome p.body + p.body{margin-top:14px}
.down{width:54px;height:54px;border-radius:50%;background:var(--purple);margin:24px auto 0;display:flex;align-items:center;justify-content:center}

/* values */
.values{top:1108px;height:315px;background:var(--purple);display:flex;justify-content:center;gap:92px;padding-top:58px}
.value{width:124px;text-align:center;color:var(--white);font-family:"Montserrat",sans-serif;font-weight:500;font-size:17px;line-height:24px}
.value .ring{width:124px;height:124px;border-radius:50%;border:3px solid var(--white);display:flex;align-items:center;justify-content:center;margin-bottom:14px}
.value .ring.active{background:var(--white)}

/* services */
.services{top:1423px;height:842px;background:var(--lavender)}
.section-title{text-align:center;font-size:40px;color:var(--purple);font-weight:700}
.services .section-title{margin-top:58px}
.group-title{font-family:"Montserrat",sans-serif;font-size:42px;font-weight:500;color:var(--ink)}
.services .group-title{position:absolute;left:78px;top:170px}
.svc-list{position:absolute;list-style:none}
.services .svc-list{left:78px;top:262px;width:500px}
.svc{display:flex;gap:22px;margin-bottom:34px}
.svc > div:last-child{min-width:0;flex:1}
.svc-icon{flex:0 0 52px;height:52px;display:flex;align-items:flex-start;justify-content:center}
.svc h4{font-size:19px;font-weight:600;color:var(--ink);margin-bottom:6px}
.svc p{font-size:13px;line-height:22px;color:var(--text)}
.ehr-photo{position:absolute;right:0;top:265px;width:590px;height:577px;background:linear-gradient(160deg,#f4f1f9 0%,#e6e2ee 50%,#c8c6d6 100%)}

/* IT */
.it{top:2265px;height:919px}
.it-photo{position:absolute;left:0;top:150px;width:570px;height:640px;background:radial-gradient(ellipse at 45% 45%,#6b62a8 0%,#3c3a6a 40%,#ffffff 72%)}
.it .group-title{position:absolute;left:590px;top:74px}
.it .svc-list{left:590px;top:146px;width:545px}
.it .svc{margin-bottom:26px}
.it .svc p{font-size:12.5px;line-height:21px}

/* about */
.about{top:3184px;height:376px;background:linear-gradient(135deg,var(--purple) 0%,var(--purple-dark) 100%);text-align:center;color:var(--white)}
.about h2{font-size:44px;font-weight:500;margin-top:56px;letter-spacing:1px}
.about p{width:720px;margin:16px auto 0;font-size:14px;line-height:26px}
.btn-outline{border:2px solid var(--white);color:var(--white);padding:13px 26px;margin-top:30px}

/* blog */
.blog{top:3560px;height:557px}
.blog .section-title{margin-top:46px}
.posts{position:absolute;top:134px;left:78px;display:flex;gap:28px}
.post{width:346px}
.post-photo{position:relative;height:210px;background:linear-gradient(135deg,#a7b8c6,#e0d8cd)}
.date{position:absolute;left:0;top:0;width:76px;height:78px;background:var(--purple);color:var(--white);text-align:center;font-family:"Montserrat",sans-serif}
.date b{display:block;font-size:34px;line-height:46px}
.date span{font-size:13px}
.post h3{font-size:16px;font-weight:600;color:var(--ink);line-height:25px;margin-top:18px}
.post p{font-size:13px;line-height:22px;color:var(--muted);margin-top:12px}

/* footer */
.site-footer{top:4117px;height:475px;background:var(--footer);color:#c9c6cf}
.foot-col{position:absolute;top:34px}
.foot-col h4{color:var(--purple-soft);font-size:18px;font-weight:600;margin-bottom:18px}
.links{left:78px;list-style:none}
.links li{font-size:13px;margin-bottom:18px;display:flex;align-items:center;gap:14px}
.links li::before{content:"";width:5px;height:5px;border-radius:50%;background:var(--purple-soft)}
.contact{left:350px;width:300px}
.contact .row{display:flex;gap:16px;font-size:13px;line-height:22px;margin-bottom:18px}
.contact-panel{position:absolute;right:0;top:0;width:480px;height:475px;background:var(--purple);padding:34px 60px 0 62px;color:var(--white)}
.contact-panel h4{font-size:24px;font-weight:600;margin-bottom:8px}
.contact-panel p{font-size:13px;line-height:20px;margin-bottom:14px}
.field{background:var(--white);height:44px;margin-bottom:12px;color:#9a97a2;font-size:12px;padding:12px 14px}
.field.tall{height:78px}
.btn-submit{display:block;width:132px;margin:14px auto 0;border:2px solid var(--white);text-align:center;padding:10px 0;font-size:15px}
.bottom-bar{position:absolute;left:0;bottom:0;width:720px;height:56px;border-top:1px solid #2b2930;display:flex;align-items:center;justify-content:space-between;padding:0 30px 0 78px;font-size:13px}
.social{display:flex;gap:10px}
.social span{width:36px;height:36px;border-radius:50%;border:1.5px solid #8a8790}
</style>
</head>
<body>

<header class="site-header">
  <div class="brand"><div class="brand-name">ClearPath</div><div class="brand-tag">HEALTHCARE SOLUTIONS</div></div>
  <div class="phone">
    <svg width="20" height="20" viewBox="0 0 24 24"><path fill="#fff" d="M6.6 10.8a15 15 0 0 0 6.6 6.6l2.2-2.2a1 1 0 0 1 1-.25 11.4 11.4 0 0 0 3.6.57 1 1 0 0 1 1 1V20a1 1 0 0 1-1 1A17 17 0 0 1 3 4a1 1 0 0 1 1-1h3.5a1 1 0 0 1 1 1c0 1.25.2 2.45.57 3.570a1 1 0 0 1-.25 1z"/></svg>
    555-014-2291
  </div>
  <nav class="main-nav">
    <span>HOME ▾</span><span>ABOUT US</span><span>SERVICES PROVIDED</span><span>BLOG</span><span>CONTACT US</span>
    <span class="search"><svg width="14" height="14" viewBox="0 0 24 24"><circle cx="10" cy="10" r="7" fill="none" stroke="#6a3fa6" stroke-width="3"/><path d="M15 15l6 6" stroke="#6a3fa6" stroke-width="3"/></svg></span>
  </nav>
</header>

<section class="hero">
  <div class="hero-photo" role="img" aria-label="Healthcare professional holding a tablet in a clinical setting"></div>
  <div class="arrow" style="left:18px"><svg width="16" height="16" viewBox="0 0 16 16"><path d="M10 2L4 8l6 6" fill="none" stroke="#fff" stroke-width="2.5"/></svg></div>
  <div class="arrow" style="right:18px"><svg width="16" height="16" viewBox="0 0 16 16"><path d="M6 2l6 6-6 6" fill="none" stroke="#fff" stroke-width="2.5"/></svg></div>
  <div class="hero-copy">
    <h1>Increasing the value and security of your <span>technology resources</span></h1>
    <p>Partner with customers to increase the value of their technology tools</p>
    <a class="btn btn-solid">GET FREE CONSULTATION</a>
  </div>
</section>

<section class="welcome">
  <h2>WELCOME TO ClearPath</h2>
  <div class="sub">HEALTHCARE SOLUTIONS</div>
  <p class="body">Lorem Ipsum is simply dummy text of the printing and typesetting industry. Lorem Ipsum has been the industry's standard dummy text ever since the 1500s, when an unkno.</p>
  <p class="body">Lorem Ipsum is simply dummy text of the printing and typesetting industry. Lorem Ipsum has been the industry's standard dummy text ever since the 1500s, when an unknown printer took a galley of type and scrambled it to make a type specimen book. It has survived not only five centuries, but also the</p>
  <div class="down"><svg width="18" height="18" viewBox="0 0 18 18"><path d="M3 6l6 6 6-6" fill="none" stroke="#fff" stroke-width="2.5"/></svg></div>
</section>

<section class="values">
  <div class="value"><div class="ring active"><svg width="56" height="56" viewBox="0 0 56 56"><circle cx="26" cy="24" r="15" fill="none" stroke="#6a3fa6" stroke-width="4"/><path d="M37 35l12 12" stroke="#6a3fa6" stroke-width="5"/><circle cx="26" cy="20" r="5" fill="#6a3fa6"/><path d="M17 32a9 9 0 0 1 18 0z" fill="#6a3fa6"/></svg></div>Customer Focused</div>
  <div class="value"><div class="ring"><svg width="56" height="56" viewBox="0 0 56 56" fill="none" stroke="#fff" stroke-width="3"><path d="M28 8v38M14 14h28M18 46h20"/><path d="M14 14l-7 16h14zM42 14l-7 16h14z"/></svg></div>Integrity &amp; Ethics</div>
  <div class="value"><div class="ring"><svg width="56" height="56" viewBox="0 0 56 56" fill="none" stroke="#fff" stroke-width="3"><rect x="12" y="8" width="32" height="40" rx="3"/><path d="M19 20l3 3 5-6M19 32l3 3 5-6M31 21h8M31 33h8"/></svg></div>Practice Accountability</div>
  <div class="value"><div class="ring"><svg width="56" height="56" viewBox="0 0 56 56" fill="none" stroke="#fff" stroke-width="3"><path d="M44 10c-12 0-20 8-24 18l8 8c10-4 18-12 18-24z"/><circle cx="35" cy="20" r="3"/><path d="M20 28l-8 2-2 6 8-2M28 36l-2 8 6-2 2-8M14 42l-4 4"/></svg></div>Professional Development</div>
  <div class="value"><div class="ring"><svg width="56" height="56" viewBox="0 0 56 56"><circle cx="28" cy="12" r="5" fill="#fff"/><path d="M10 18l14 8-4 20h6l4-14 6 14h6l-8-20 12-10-3-3-12 8h-6L12 14z" fill="#fff"/></svg></div>Have Fun</div>
</section>

<section class="services">
  <h2 class="section-title">Services We Provided</h2>
  <h3 class="group-title">Electronic Health Record</h3>
  <div class="ehr-photo" role="img" aria-label="Physician holding a tablet showing an electronic health record system"></div>
  <ul class="svc-list">
    <li class="svc"><div class="svc-icon"><svg width="44" height="44" viewBox="0 0 44 44" fill="none" stroke="#6a3fa6" stroke-width="2.5"><rect x="4" y="6" width="32" height="32" rx="2"/><path d="M10 16h12M10 24h20M10 31h14"/><circle cx="34" cy="10" r="6"/></svg></div><div><h4>EHR Optimization Services</h4><p>Provide guidance and resources to assist with improving the effective use of the customer's EHR system</p></div></li>
    <li class="svc"><div class="svc-icon"><svg width="44" height="44" viewBox="0 0 44 44" fill="none" stroke="#6a3fa6" stroke-width="2.5"><rect x="8" y="6" width="28" height="34" rx="2"/><rect x="16" y="3" width="12" height="6" fill="#fff"/><path d="M14 18h16M14 25h16M14 32h10"/></svg></div><div><h4>EHR Implementation</h4><p>Assist or conduct a complete EHR implementation</p></div></li>
    <li class="svc"><div class="svc-icon"><svg width="44" height="44" viewBox="0 0 44 44" fill="none" stroke="#6a3fa6" stroke-width="2.5"><rect x="10" y="4" width="24" height="36" rx="3"/><path d="M22 15v12M16 21h12"/></svg></div><div><h4>EHR Assessment</h4><p>Provide a high-level assessment of an organization and how they are currently utilizing this system</p></div></li>
    <li class="svc"><div class="svc-icon"><svg width="44" height="44" viewBox="0 0 44 44" fill="none" stroke="#6a3fa6" stroke-width="2.5"><circle cx="22" cy="17" r="12"/><path d="M22 11l2 4 4 .5-3 3 1 4-4-2-4 2 1-4-3-3 4-.5zM15 27l-4 13 6-3 3 5 2-12M29 27l4 13-6-3-3 5"/></svg></div><div><h4>EHR Quality Assessment</h4><p>Provide a customized quality assessment to assist with improving quality indicator scores.</p></div></li>
    <li class="svc"><div class="svc-icon"><svg width="44" height="44" viewBox="0 0 44 44" fill="none" stroke="#6a3fa6" stroke-width="2.5"><path d="M8 26v-6a14 14 0 0 1 28 0v6"/><rect x="5" y="24" width="7" height="11" rx="2"/><rect x="32" y="24" width="7" height="11" rx="2"/><circle cx="22" cy="20" r="6"/><path d="M36 35c0 4-6 5-11 5"/></svg></div><div><h4>On-Going EHR Support</h4><p>Provide on-going support for an organization on a monthly fee basis</p></div></li>
  </ul>
</section>

<section class="it">
  <div class="it-photo" role="img" aria-label="Tablet displaying medical scans with a stethoscope"></div>
  <h3 class="group-title">Information Technology</h3>
  <ul class="svc-list">
    <li class="svc"><div class="svc-icon"><svg width="44" height="44" viewBox="0 0 44 44"><path d="M22 4l16 6v10c0 10-7 17-16 20C13 37 6 30 6 20V10z" fill="#6a3fa6"/><path d="M22 4v36C13 37 6 30 6 20V10z" fill="#8a6ac0"/></svg></div><div><h4>Risk Assessment</h4><p>Provide comprehensive risk assessment including identifying all risks associated with the customer's electronic protected health information (ePHI).</p></div></li>
    <li class="svc"><div class="svc-icon"><svg width="44" height="44" viewBox="0 0 44 44" fill="#6a3fa6"><circle cx="22" cy="10" r="5"/><circle cx="9" cy="18" r="4"/><circle cx="35" cy="18" r="4"/><path d="M13 30a9 9 0 0 1 18 0v4H13zM2 32a7 7 0 0 1 12-5v7H2zM42 32a7 7 0 0 0-12-5v7h12z"/></svg></div><div><h4>Policy Management and Consulting</h4><p>Provide guidance on IT policy management, particularly policies required and recommended by national Health Insurance Portability and Accountability Act (HIPAA) guidelines.</p></div></li>
    <li class="svc"><div class="svc-icon"><svg width="44" height="44" viewBox="0 0 44 44"><path d="M22 4l16 6v10c0 10-7 17-16 20C13 37 6 30 6 20V10z" fill="#6a3fa6"/><path d="M22 12l2.5 5 5.5.8-4 3.9 1 5.5-5-2.6-5 2.6 1-5.5-4-3.9 5.5-.8z" fill="#fff"/></svg></div><div><h4>Chief Information Officer</h4><p>Act as the organization's CIO or IT Director to assist with improving department's functions and effectiveness.</p></div></li>
    <li class="svc"><div class="svc-icon"><svg width="44" height="44" viewBox="0 0 44 44" fill="#6a3fa6"><path d="M12 6h20l-3 8H15z"/><circle cx="22" cy="20" r="7"/><path d="M8 40a14 12 0 0 1 28 0z"/><path d="M33 24l7 3v5c0 4-3 7-7 8-4-1-7-4-7-8v-5z" fill="#8a6ac0"/></svg></div><div><h4>Chief Information Security Officer</h4><p>Act as the organization's CISO or Information Security Officer to assist with improving department's functions and effectiveness</p></div></li>
    <li class="svc"><div class="svc-icon"><svg width="44" height="44" viewBox="0 0 44 44"><rect x="8" y="4" width="28" height="36" rx="2" fill="#6a3fa6"/><path d="M14 14l3 3 5-6M14 26l3 3 5-6M26 15h5M26 27h5" stroke="#fff" stroke-width="2.5" fill="none"/></svg></div><div><h4>IT Department Evaluation</h4><p>Evaluate the department to determine potential changes or issues based on customer perceptions of department</p></div></li>
    <li class="svc"><div class="svc-icon"><svg width="44" height="44" viewBox="0 0 44 44"><path d="M8 26v-6a14 14 0 0 1 28 0v6" fill="none" stroke="#6a3fa6" stroke-width="3"/><rect x="5" y="24" width="7" height="11" rx="2" fill="#6a3fa6"/><rect x="32" y="24" width="7" height="11" rx="2" fill="#6a3fa6"/><circle cx="22" cy="22" r="7" fill="#6a3fa6"/></svg></div><div><h4>On-Going CIO or CISO Support</h4><p>Provide on-going support for an organization on a monthly fee basis</p></div></li>
  </ul>
</section>

<section class="about">
  <h2>ABOUT US</h2>
  <p>Lorem Ipsum is simply dummy text of the printing and typesetting industry. Lorem Ipsum has been the industry's standard dummy text ever since the 1500s, when an unknown printer took a galley of type and scrambled it to make a type specimen book. It has survived not only five centuries, but also the</p>
  <a class="btn btn-outline">MEET OUR TEAM</a>
</section>

<section class="blog">
  <h2 class="section-title">Latest Blog Post</h2>
  <div class="posts">
    <article class="post">
      <div class="post-photo" role="img" aria-label="Care team meeting around a tablet"><div class="date"><b>25</b><span>Oct</span></div></div>
      <h3>Lorem Ipsum is simply dummy text of the printing and typesetting industry.</h3>
      <p>Lorem Ipsum is simply dummy text of the printing and typesetting industry. Lorem Ipsum has been the industry's standard dummy text...[...]</p>
    </article>
    <article class="post">
      <div class="post-photo" role="img" aria-label="Doctor greeting a patient with a handshake" style="background:linear-gradient(135deg,#7d9cc0,#d8d4d2)"><div class="date"><b>25</b><span>Oct</span></div></div>
      <h3>Lorem Ipsum is simply dummy text of the printing and typesetting industry.</h3>
      <p>Lorem Ipsum is simply dummy text of the printing and typesetting industry. Lorem Ipsum has been the industry's standard dummy text...[...]</p>
    </article>
    <article class="post">
      <div class="post-photo" role="img" aria-label="Professional woman working at a laptop" style="background:linear-gradient(135deg,#e8e6ea,#bfbcc6)"><div class="date"><b>25</b><span>Oct</span></div></div>
      <h3>Lorem Ipsum is simply dummy text of the printing and typesetting industry.</h3>
      <p>Lorem Ipsum is simply dummy text of the printing and typesetting industry. Lorem Ipsum has been the industry's standard dummy text...[...]</p>
    </article>
  </div>
</section>

<footer class="site-footer">
  <div class="foot-col links">
    <h4>QUICK LINKS</h4>
    <ul class="links" style="position:static"><li>Home</li><li>About Us</li><li>Services We Provided</li><li>Blog</li><li>Contact Us</li></ul>
  </div>
  <div class="foot-col contact">
    <h4>CONTACT INFO</h4>
    <div class="row"><svg width="18" height="22" viewBox="0 0 18 22"><path d="M9 1a8 8 0 0 0-8 8c0 6 8 12 8 12s8-6 8-12a8 8 0 0 0-8-8z" fill="#8a6ac0"/><circle cx="9" cy="9" r="3" fill="#121115"/></svg><div>ClearPath Health<br>101 - Lorem ipsum simple text<br>of print and type industry.</div></div>
    <div class="row"><svg width="18" height="18" viewBox="0 0 24 24"><path fill="#8a6ac0" d="M6.6 10.8a15 15 0 0 0 6.6 6.6l2.2-2.2a1 1 0 0 1 1-.25 11.4 11.4 0 0 0 3.6.57 1 1 0 0 1 1 1V20a1 1 0 0 1-1 1A17 17 0 0 1 3 4a1 1 0 0 1 1-1h3.5a1 1 0 0 1 1 1c0 1.25.2 2.45.57 3.57a1 1 0 0 1-.25 1z"/></svg><div>555-014-2291</div></div>
    <div class="row"><svg width="18" height="18" viewBox="0 0 24 24"><rect x="2" y="5" width="20" height="14" rx="2" fill="#8a6ac0"/><path d="M3 6l9 7 9-7" fill="none" stroke="#121115" stroke-width="2"/></svg><div>contact@clearpathhealth.example</div></div>
  </div>
  <div class="bottom-bar">
    <span>©ClearPath Health - 2018 All Right Reserved.</span>
    <div class="social"><span></span><span></span><span></span></div>
  </div>
  <div class="contact-panel">
    <h4>CONTACT US</h4>
    <p>If you need an have any question please<br>contact Us Today !</p>
    <div class="field">Name *</div>
    <div class="field">Email *</div>
    <div class="field">Phone *</div>
    <div class="field tall">Message *</div>
    <a class="btn btn-submit">SUBMIT</a>
  </div>
</footer>

</body>
</html>
```